Business card design needed for Automotive Reconditioning business

I have a logo design i just cant decide on the best color or layout for the business card, I will upload all the files so you can see all colors schemes we are considering. I have other file formats if needed let me know.

Target Market(s)

automotive dealerships

Contact Information for Business Card

HERE are the Descriptions and info needed on the card:
Interior Repair: Leather carpet burns panels dash Deoderize
Dealer products and Vin Verify
( spot for name and cell number) My name is Norman Bexley phone 614 352-4180 Title COO www.QuorvalMotive.com

Font styles to use
Sans Serif
Other font styles liked:
• what ever you think looks best

Requirements
Must have
• Must be able to change the name and phone for employees

```html
<!DOCTYPE html>
<html lang="en">
<head>
<meta charset="utf-8">
<title>Quorval Motive Reconditioning Corp. – Business Card</title>
<link rel="stylesheet" href="https://fonts.googleapis.com/css2?family=Exo+2:wght@400;600;800&display=swap">
<style>
  :root {
    --page-bg: #d9dde2;
    --card-bg: #232323;
    --accent-green: #8dc63f;
    --emboss-dark: #1a1a1a;
    --emboss-light: #3a3a3a;
    --muted-grey: #8a8a8a;
    --text-light: #e6e6e6;
  }
  * { box-sizing: border-box; margin: 0; padding: 0; }
  html, body {
    width: 1200px;
    height: 800px;
    overflow: hidden;
    background: var(--page-bg);
  }
  .canvas {
    width: 1200px;
    height: 800px;
    display: flex;
    align-items: center;
    justify-content: center;
  }
  .business-card {
    position: relative;
    width: 1050px;
    height: 600px;
    background: var(--card-bg);
    font-family: "Exo 2", sans-serif;
    overflow: hidden;
    box-shadow: 0 10px 30px rgba(0,0,0,0.25);
  }
  .brand {
    position: absolute;
    left: 280px;
    top: 140px;
    width: 480px;
    display: flex;
    align-items: center;
    gap: 16px;
  }
  .brand-square {
    width: 30px;
    height: 30px;
    background: var(--accent-green);
    flex: none;
  }
  .brand-name {
    font-weight: 800;
    font-size: 30px;
    line-height: 1.15;
    letter-spacing: 1px;
    text-transform: uppercase;
    color: var(--accent-green);
    white-space: nowrap;
  }
  .person {
    position: absolute;
    right: 490px;
    top: 318px;
    text-align: right;
    white-space: nowrap;
  }
  .person-name {
    font-weight: 800;
    font-size: 42px;
    line-height: 1.1;
    letter-spacing: 2px;
    text-transform: uppercase;
    color: var(--emboss-dark);
    text-shadow: -1px -1px 0 var(--emboss-light), 2px 2px 2px rgba(0,0,0,0.6);
  }
  .person-title {
    font-weight: 600;
    font-size: 20px;
    letter-spacing: 1px;
    color: var(--emboss-dark);
    text-shadow: -1px -1px 0 var(--emboss-light);
  }
  .divider {
    position: absolute;
    left: 580px;
    top: 305px;
    width: 2px;
    height: 90px;
    background: var(--muted-grey);
  }
  .contact {
    position: absolute;
    left: 605px;
    top: 312px;
    list-style: none;
    display: flex;
    flex-direction: column;
    gap: 12px;
    color: var(--text-light);
    white-space: nowrap;
  }
  .contact-item {
    display: flex;
    align-items: center;
    gap: 12px;
    font-size: 22px;
  }
  .contact-item svg { flex: none; }
  .services {
    position: absolute;
    left: 40px;
    bottom: 50px;
    font-size: 26px;
    color: var(--text-light);
    letter-spacing: 0.5px;
    white-space: nowrap;
  }
  .accent-stripe {
    position: absolute;
    left: 0;
    right: 0;
    bottom: 0;
    height: 10px;
    background: var(--accent-green);
  }
</style>
</head>
<body>
<main class="canvas">
  <section class="business-card">
    <header class="brand">
      <span class="brand-square"></span>
      <span class="brand-name">Quorval Motive<br>Reconditioning Corp.</span>
    </header>

    <div class="person">
      <p class="person-name">Norman Bexley</p>
      <p class="person-title">COO</p>
    </div>

    <span class="divider"></span>

    <ul class="contact">
      <li class="contact-item">
        <svg width="16" height="24" viewBox="0 0 16 24" aria-hidden="true">
          <rect x="1.5" y="1.5" width="13" height="21" rx="2" fill="none" stroke="#e6e6e6" stroke-width="2"/>
          <line x1="6" y1="19" x2="10" y2="19" stroke="#e6e6e6" stroke-width="2"/>
        </svg>
        <span>614 352-4180</span>
      </li>
      <li class="contact-item">
        <svg width="16" height="24" viewBox="0 0 16 24" aria-hidden="true">
          <circle cx="8" cy="9" r="6" fill="none" stroke="#e6e6e6" stroke-width="2"/>
          <line x1="4" y1="14" x2="1" y2="21" stroke="#e6e6e6" stroke-width="2"/>
        </svg>
        <span>www.QuorvalMotive.com</span>
      </li>
    </ul>

    <p class="services">Leather carpet burns panels dash Deoderize Dealer products and Vin Verify</p>
    <div class="accent-stripe"></div>
  </section>
</main>
</body>
</html>
```